Business Card Design

We need a design for business cards for our company. We have a logo. We teach EMT's and we are based out of Virginia. The information that will need to add would be, name, title, phone number, email, address. On the back of the business card would be "We help you, help others"

Target Market(s)

People that want to become EMT's

Colors

Designer to choose colors to be used in the design.

Requirements
Must have
• company logo

```html
<!DOCTYPE html>
<html lang="en">
<head>
<meta charset="utf-8">
<title>Varden Rescue Academy – Business Cards</title>
<link href="https://fonts.googleapis.com/css2?family=Lato:wght@300;400;700;900&display=swap" rel="stylesheet">
<style>
  :root {
    --page: #1b1c1f;
    --card: #1d2233;
    --card-light: #242a3d;
    --pattern: #2c3446;
    --red: #ee2a42;
    --grey: #7d8893;
    --text-light: #c7ccd6;
    --white: #ffffff;
  }
  * { margin: 0; padding: 0; box-sizing: border-box; }
  html, body {
    width: 1200px; height: 900px; overflow: hidden;
    background: var(--page);
    font-family: "Lato", sans-serif;
  }
  .canvas { position: relative; width: 1200px; height: 900px; }
  .card {
    position: absolute; width: 665px; height: 380px;
    background: radial-gradient(ellipse at 70% 30%, var(--card-light), var(--card) 70%);
    overflow: hidden;
    box-shadow: 0 18px 40px rgba(0,0,0,.55);
  }
  .card--back { left: 150px; top: 50px; }
  .card--front { left: 385px; top: 470px; }

  .pattern-area {
    position: absolute; inset: 0;
    background: radial-gradient(ellipse 320px 300px at 88% 30%, rgba(60,72,92,.5), rgba(44,52,70,.2) 60%, rgba(29,34,51,0) 100%);
  }
  .wordmark {
    position: absolute; right: 40px; top: 48px;
    display: flex; align-items: center; gap: 12px;
  }
  .wordmark__dot { width: 14px; height: 14px; border-radius: 50%; background: var(--red); }
  .wordmark__name {
    font-weight: 700; font-size: 27px; color: var(--red);
    letter-spacing: .5px; text-transform: uppercase;
  }

  .tagline {
    position: absolute; left: 40px; bottom: 48px;
    font-size: 25px; letter-spacing: 1px; text-transform: uppercase;
  }
  .tagline__lead { color: var(--red); font-weight: 900; }
  .tagline__rest { color: var(--text-light); font-weight: 300; }

  .person { position: absolute; right: 265px; top: 236px; text-align: right; }
  .person__name { font-size: 24px; text-transform: uppercase; color: var(--red); white-space: nowrap; }
  .person__first { font-weight: 900; }
  .person__last { font-weight: 300; }
  .person__title { color: var(--white); font-size: 14px; margin-top: 4px; }

  .contacts {
    position: absolute; left: 420px; top: 192px;
    list-style: none; font-size: 14px; color: var(--white);
  }
  .contacts li { display: flex; align-items: center; gap: 10px; height: 24px; white-space: nowrap; }
  .contacts svg { width: 14px; height: 14px; fill: var(--red); flex: none; }
  .contacts .contacts__web { color: var(--red); font-weight: 700; padding-left: 24px; }

  .edge-bands { position: absolute; left: 0; bottom: 0; width: 665px; height: 60px; }
</style>
</head>
<body>
<main class="canvas">

  <section class="card card--back" aria-label="Business card back">
    <div class="pattern-area" role="img" aria-label="Faint medical cross pattern"></div>
    <div class="wordmark">
      <span class="wordmark__dot"></span>
      <span class="wordmark__name">Varden Rescue Academy</span>
    </div>
    <p class="tagline">
      <span class="tagline__lead">We help you,</span>
      <span class="tagline__rest">help others</span>
    </p>
  </section>

  <section class="card card--front" aria-label="Business card front">
    <div class="pattern-area" role="img" aria-label="Faint medical cross pattern"></div>
    <div class="wordmark">
      <span class="wordmark__dot"></span>
      <span class="wordmark__name">Varden Rescue Academy</span>
    </div>

    <div class="person">
      <p class="person__name"><span class="person__first">Dana</span> <span class="person__last">Kerrow</span></p>
      <p class="person__title">Founder / Director</p>
    </div>

    <ul class="contacts">
      <li>
        <svg viewBox="0 0 24 24" aria-hidden="true"><path d="M6.6 10.8a15 15 0 0 0 6.6 6.6l2.2-2.2a1 1 0 0 1 1-.25 11.4 11.4 0 0 0 3.6.57 1 1 0 0 1 1 1V20a1 1 0 0 1-1 1A17 17 0 0 1 3 4a1 1 0 0 1 1-1h3.5a1 1 0 0 1 1 1c0 1.25.2 2.45.57 3.57a1 1 0 0 1-.25 1z"/></svg>
        <span>+1 540 555 0142</span>
      </li>
      <li>
        <svg viewBox="0 0 24 24" aria-hidden="true"><path d="M2 5h20v14H2zm2 2v.5l8 5 8-5V7l-8 5z"/></svg>
        <span>info@vardenrescue.com</span>
      </li>
      <li class="contacts__web">www.vardenrescue.com</li>
    </ul>

    <svg class="edge-bands" viewBox="0 0 665 60" aria-hidden="true">
      <rect x="290" y="40" width="375" height="20" fill="var(--grey)"/>
      <path d="M0 44 H262 Q300 44 305 60 H0 Z" fill="var(--red)"/>
    </svg>
  </section>

</main>
</body>
</html>
```